Green Logistics / Last Mile Delivery Firm needs cool one-page website

FYI - We do have a detailed brief in the uploaded files section below
COMPANY
We recently launched the company Brook Logistics which is a pioneer in urban green logistics and provides zero-emissions last mile delivery services (i.e. delivery of parcels with delivery vans to the doorstep of households) for its logistics and retail clients.
We take on urban parcel delivery for our clients with a 100% electric commercial vehicles fleet, fair and sustainable working conditions for our employees and an unparalleled professional and customer-focused mindset.
WEBSITE
In the detailed brief, we have provided examples to emulate. We need the design + coding of the website. Website needs to be friendly/optimized for and should open swiftly on both Android & iOS.
In general, the website should convey
- green mission of the company
- sustainability (good working conditions, focus on employees)
- customer orientation
- professionalism
DESIGN
In the detailed brief, we have provided designs to emulate.
Color design: we do have a logo which features 2 green colors (one lighter and one darker color tone). However, the colors on the website do not necessarily need to follow these 2 colors exactly as we are able to switch the logo colors.
Imagery: should reflect maybe 50% green/leaf/tree , 25% customer and employee orientation, and 25% logistics (here it's important that it is the last mile delivery, i.e. delivery with delivery vans to the doorstep of households)
Coding

```html
<!DOCTYPE html>
<html lang="en">
<head>
<meta charset="utf-8">
<title>Brook Logistics – Sustainable Last Mile</title>
<link href="https://fonts.googleapis.com/css2?family=Roboto:wght@400;500;700&family=Mulish:ital,wght@0,400;0,600;0,700;1,400&display=swap" rel="stylesheet">
<style>
:root{
  --lime:#8cc63f;
  --green:#3aa935;
  --ink:#1f1f1f;
  --text:#555;
  --muted:#7a7a7a;
  --line:#e4e4e4;
  --soft:#f6f6f6;
  --dark:#0b1a09;
  --white:#fff;
}
*{box-sizing:border-box;margin:0;padding:0}
html,body{width:1200px;height:3328px;overflow:hidden}
body{font-family:"Mulish",sans-serif;color:var(--text);background:var(--white);position:relative}
.abs{position:absolute}
h1,h2,h3,h4{font-family:"Roboto",sans-serif;color:var(--ink);font-weight:500}

/* top bar */
.topbar{top:0;left:0;width:1200px;height:36px;font-size:10px;color:#444}
.topbar .item{top:12px;display:flex;align-items:center;gap:8px}
.lang{top:12px;left:927px;font-size:10px}
.lang::after{content:"";display:inline-block;width:4px;height:4px;border-right:1px solid #666;border-bottom:1px solid #666;transform:rotate(45deg);margin-left:14px;position:relative;top:-2px}

/* header */
.header{top:36px;left:0;width:1200px;height:76px;background:var(--soft)}
.brand{left:225px;top:20px;display:flex;align-items:center;gap:8px;font-family:"Roboto",sans-serif;font-weight:700;font-size:19px;color:var(--green)}
.brand .dot{width:30px;height:30px;border-radius:50%;background:var(--green)}
.nav{right:225px;top:33px;display:flex;gap:30px;font-size:11px;color:#333;letter-spacing:.3px}
.nav .active{color:var(--green)}

/* hero */
.hero{top:112px;left:0;width:1200px;height:562px;background:radial-gradient(ellipse at 50% 45%,#2f5d1e 0%,#1c3d12 45%,#0e240a 100%)}
.hero h1{position:absolute;top:208px;width:100%;text-align:center;color:var(--white);font-size:31px;font-weight:700}
.hero .sub{position:absolute;top:259px;width:100%;text-align:center;color:var(--white);font-size:14px;letter-spacing:.3px}
.btn{display:flex;align-items:center;justify-content:center;background:var(--lime);color:#1d2a10;font-size:11px;font-weight:600}
.hero .btn{position:absolute;left:522px;top:321px;width:156px;height:32px}
.arrow{width:24px;height:24px;border:1.5px solid var(--white);border-radius:50%;top:269px;display:flex;align-items:center;justify-content:center}
.dots{top:536px;left:553px;display:flex;gap:9px}
.dots i{width:8px;height:8px;border:1.3px solid var(--lime);border-radius:50%}
.dots i.on{background:var(--lime)}

/* section titles */
.sec-title{width:1200px;left:0;text-align:center;font-size:22px;font-weight:500}
.rule{left:558px;width:84px;height:10px}

/* about */
.about-card{top:798px;width:238px}
.about-card .pic{height:144px}
.about-card .badge{position:absolute;top:123px;left:14px;width:42px;height:42px;border-radius:50%;background:var(--white);box-shadow:0 1px 4px rgba(0,0,0,.15);display:flex;align-items:center;justify-content:center}
.about-card h3{margin-top:38px;font-size:13px}
.about-card p{font-size:9.5px;line-height:17.5px;margin-top:10px}
.about-card p+p{margin-top:8px}
.is-title{left:225px;top:1216px;font-size:22px}
.compare{left:225px;top:1276px;width:750px;height:281px;background:var(--soft)}
.compare .divider{left:375px;top:0;width:1px;height:281px;background:#d8d8d8}
.compare .h-left{right:405px;top:45px;font-family:"Roboto",sans-serif;font-size:16px;color:#333}
.compare .h-right{left:406px;top:45px;font-family:"Roboto",sans-serif;font-size:16px;color:var(--ink);font-weight:500}
.row{left:0;width:750px;height:24px}
.row .old{position:absolute;right:405px;top:6px;font-size:9.5px;color:#555;text-decoration:line-through}
.row .num{position:absolute;left:364px;top:0;width:23px;height:23px;border-radius:50%;background:var(--lime);color:var(--white);font-size:9px;display:flex;align-items:center;justify-content:center}
.row .new{position:absolute;left:406px;top:5px;font-size:10.5px;color:var(--green);font-weight:600}

/* services */
.services{top:1588px;left:0;width:1200px;height:453px;background:#f8f8f8}
.services .intro{position:absolute;top:112px;width:1200px;text-align:center;font-size:9.5px;line-height:17.5px}
.svc{top:189px;width:180px;height:214px;background:var(--white);text-align:center}
.svc .pic{height:106px}
.svc h4{font-size:11px;margin-top:20px}
.svc p{font-size:9.5px;line-height:16.5px;margin:10px 14px 0;color:var(--muted)}

/* cta */
.cta{top:2041px;left:0;width:1200px;height:169px;background:var(--dark)}
.cta h2{position:absolute;left:225px;top:50px;color:var(--white);font-size:22px;font-weight:700}
.cta p{position:absolute;left:225px;top:93px;width:500px;color:var(--white);font-size:9.5px;line-height:17.5px}
.cta .btn{position:absolute;left:819px;top:69px;width:156px;height:32px}

/* careers */
.careers-left{left:225px;top:2340px;width:360px;font-size:9.5px;line-height:16.5px}
.careers-left p{margin-bottom:16px}
.careers-left .short{width:24px;height:2px;background:var(--green);margin:10px 0 14px}
.careers-left em{color:#444}
.careers-left .interest{font-size:12px;color:#333;margin:16px 0 10px}
.btn-out{display:flex;align-items:center;justify-content:center;border:1px solid var(--lime);font-size:11px;color:#333;background:var(--white)}
.careers-right{left:608px;top:2340px;width:367px;font-size:9.5px;line-height:16.5px}
.acc{left:608px;width:367px;border:1px solid var(--line);font-size:9.5px;font-weight:700;color:#333;padding:0 12px;display:flex;align-items:center;justify-content:space-between}
.acc.open{color:var(--green)}
.panel{left:608px;top:2433px;width:367px;height:233px;border:1px solid var(--line);border-top:none;padding:38px 14px 0 14px}
.panel li{list-style:none;font-size:9.5px;line-height:16px;display:flex;gap:7px;margin-bottom:9px}
.panel li svg{flex:none;margin-top:4px}

/* contact */
.contact{top:2799px;left:0;width:1200px;height:529px;background:linear-gradient(180deg,#0c1a0a 0%,#12260d 45%,#2a4d16 78%,#3e6a1f 100%)}
.contact h2{position:absolute;top:52px;width:1200px;text-align:center;color:var(--white);font-size:22px}
.contact .lead{position:absolute;top:115px;width:1200px;text-align:center;color:var(--white);font-family:"Roboto",sans-serif;font-weight:700;font-size:11px}
.contact .note{position:absolute;top:137px;left:390px;width:420px;text-align:center;color:var(--white);font-size:9.5px;line-height:15px}
.info{left:238px;display:flex;align-items:center;gap:13px;color:var(--white);font-family:"Roboto",sans-serif;font-size:11px;font-weight:700}
.info .ic{width:36px;height:36px;border-radius:50%;background:var(--white);display:flex;align-items:center;justify-content:center}
.field{background:var(--white);font-size:9px;color:#999;padding:9px 12px}
.contact .btn{position:absolute;left:681px;top:397px;width:156px;height:31px}
.footer-line{left:225px;top:482px;width:750px;height:1px;background:rgba(255,255,255,.2)}
.foot{top:498px;color:var(--white);font-size:9px}
.foot u{margin-right:22px}
.social{top:486px;width:32px;height:32px;border-radius:50%;background:var(--white)}
</style>
</head>
<body>

<div class="abs topbar">
  <div class="abs item" style="left:225px">
    <svg width="12" height="9" viewBox="0 0 12 9"><rect x=".5" y=".5" width="11" height="8" fill="none" stroke="#3aa935"/><path d="M.5.5 6 5 11.5.5" fill="none" stroke="#3aa935"/></svg>
    info@brooklogistics.com
  </div>
  <div class="abs item" style="left:366px">
    <svg width="11" height="11" viewBox="0 0 24 24"><path d="M6.6 10.8a15 15 0 0 0 6.6 6.6l2.2-2.2c.3-.3.7-.4 1-.2 1.1.4 2.3.6 3.6.6.6 0 1 .4 1 1V20c0 .6-.4 1-1 1A17 17 0 0 1 3 4c0-.6.4-1 1-1h3.5c.6 0 1 .4 1 1 0 1.3.2 2.5.6 3.6.1.3 0 .7-.2 1z" fill="#3aa935"/></svg>
    (555) 014-2290
  </div>
  <div class="abs lang">English</div>
</div>

<header class="abs header">
  <div class="abs brand"><span class="dot"></span>Brook Logistics</div>
  <nav class="abs nav">
    <span class="active">HOME</span><span>ABOUT US</span><span>SERVICES</span><span>CAREERS</span><span>CONTACT US</span>
  </nav>
</header>

<section class="abs hero" role="img" aria-label="Dense green leaves of a hedge filling the background">
  <h1>Brook Logistics – Sustainable Last Mile</h1>
  <p class="sub">BECAUSE WE CARE ABOUT TREES!</p>
  <a class="btn">Get Started</a>
  <div class="abs arrow" style="left:200px"><svg width="8" height="10" viewBox="0 0 8 10"><path d="M6 1 2 5l4 4" fill="none" stroke="#fff" stroke-width="1.6"/></svg></div>
  <div class="abs arrow" style="left:975px"><svg width="8" height="10" viewBox="0 0 8 10"><path d="M2 1l4 4-4 4" fill="none" stroke="#fff" stroke-width="1.6"/></svg></div>
  <div class="abs dots" style="top:536px"><i></i><i></i><i class="on"></i><i></i><i></i><i></i></div>
</section>

<!-- About -->
<h2 class="abs sec-title" style="top:724px">About Us</h2>
<svg class="abs rule" style="top:757px" viewBox="0 0 84 10"><line x1="0" y1="5" x2="30" y2="5" stroke="#3aa935"/><line x1="54" y1="5" x2="84" y2="5" stroke="#3aa935"/><path d="M36 8c2-6 8-7 12-6-1 5-6 7-12 6z" fill="#3aa935"/></svg>

<article class="abs about-card" style="left:225px">
  <div class="pic" role="img" aria-label="White electric delivery van on a lime green background" style="background:linear-gradient(135deg,#9fd14a,#7cb832)"></div>
  <div class="badge"><svg width="18" height="18" viewBox="0 0 24 24"><path d="M12 3a4 4 0 0 1 4 4c0 3-4 7-4 7S8 10 8 7a4 4 0 0 1 4-4zM5 20c1-3 4-4 7-4s6 1 7 4z" fill="none" stroke="#666" stroke-width="1.3"/></svg></div>
  <h3>Who we are</h3>
  <p>Brook Logistics is a pioneer in urban green logistics and provides zeroemissions last mile delivery services for its logistics and retail clients.</p>
  <p>We take on urban parcel delivery for our clients with a 100% electric commercial vehicles fleet, fair and sustainable working conditions for our employees and an unparalleled professional and customer- focused mindset.</p>
</article>
<article class="abs about-card" style="left:481px">
  <div class="pic" role="img" aria-label="Glowing blue world map with connected network points" style="background:linear-gradient(135deg,#0e3b6e,#1e7bc7 55%,#0a2a52)"></div>
  <div class="badge"><svg width="18" height="18" viewBox="0 0 24 24"><circle cx="12" cy="12" r="8" fill="none" stroke="#666" stroke-width="1.3"/><circle cx="12" cy="12" r="4" fill="none" stroke="#666" stroke-width="1.3"/><path d="M12 12l7-7" stroke="#666" stroke-width="1.3"/></svg></div>
  <h3>Our Mission</h3>
  <p>To satisfy consumers' ever-rising desire to buy products online, the CO2 emissions from delivery traffic will increase by 32% in the top 100 cities globally until 2030.</p>
  <p>Our clients care about our planet the same way we do, which is why Brook Logistics helps to make the planet a better place by running the most environmentally friendly urban last mile possible</p>
</article>
<article class="abs about-card" style="left:737px">
  <div class="pic" role="img" aria-label="Chalkboard with a drawn light bulb and the words Our Values" style="background:linear-gradient(135deg,#1f3346,#2c4a63)"></div>
  <div class="badge"><svg width="18" height="18" viewBox="0 0 24 24"><path d="M6 5h12l3 5-9 10L3 10zM3 10h18M9 5l3 15 3-15" fill="none" stroke="#666" stroke-width="1.2"/></svg></div>
  <h3>Our values</h3>
  <p>We see ourselves as a professional services company who strongly cares about the environment, its clients and their customers, as well as its employees.</p>
  <p>We believe that delivering parcels with zero emissions and providing a unique customer experience through a highly professional attitude and a great team spirit are the cornerstones for Brook Logistics to operate in today's world in a sustainable yet profitable way.</p>
</article>

<h2 class="abs is-title">Brook Logistics is…</h2>
<div class="abs compare">
  <div class="abs divider"></div>
  <div class="abs h-left">An Ordinary Parcel Delivery Firm</div>
  <div class="abs h-right">A pioneering Green Last Mile</div>
  <div class="abs row" style="top:78px"><span class="old">Polluting our cities</span><span class="num">1</span><span class="new">Delivering parcels emissions-free</span></div>
  <div class="abs row" style="top:112px"><span class="old">Always in a rush</span><span class="num">2</span><span class="new">Putting customer experience first</span></div>
  <div class="abs row" style="top:146px"><span class="old">Short-term oriented</span><span class="num">3</span><span class="new">Operating the business sustainably</span></div>
  <div class="abs row" style="top:179px"><span class="old">Focusing on profit only</span><span class="num">4</span><span class="new">Focusing on the environment, customers and employees</span></div>
  <div class="abs row" style="top:213px"><span class="old">Yet another parcel delivery firm</span><span class="num">5</span><span class="new">A professional services company</span></div>
</div>

<!-- Services -->
<section class="abs services">
  <h2 class="abs sec-title" style="top:50px">Our Services</h2>
  <svg class="abs rule" style="top:83px" viewBox="0 0 84 10"><line x1="0" y1="5" x2="30" y2="5" stroke="#3aa935"/><line x1="54" y1="5" x2="84" y2="5" stroke="#3aa935"/><path d="M36 8c2-6 8-7 12-6-1 5-6 7-12 6z" fill="#3aa935"/></svg>
  <p class="intro">Brook Logistics provides last mile delivery services in urban areas to clients in the logistics and retail space.<br>Our permanent employees are all highly trained and commit to highest professional standards<br>which we continuously review and further develop with them.</p>
  <div class="abs svc" style="left:225px"><div class="pic" role="img" aria-label="Turquoise electric delivery van parked on a city street" style="background:linear-gradient(160deg,#9bb0c2,#3fb6d4 60%,#5a6470)"></div><h4>Zero-emission delivery</h4><p>We operate a 100% electric commercial vehicle fleet</p></div>
  <div class="abs svc" style="left:415px"><div class="pic" role="img" aria-label="Courier in a red jacket on a scooter with a delivery bag" style="background:linear-gradient(160deg,#c9c9c9,#b8432e 55%,#7b7b7b)"></div><h4>Highly trained delivery drivers</h4><p>We only employ permanently, train for above average, and live a great team spirit</p></div>
  <div class="abs svc" style="left:605px"><div class="pic" role="img" aria-label="Delivery worker handing over paper bags at a front door" style="background:linear-gradient(160deg,#e2e2e2,#c49a6c 55%,#3a4f8a)"></div><h4>Professional all around</h4><p>We honor our commitments and hold ourselves to the highest professional standards</p></div>
  <div class="abs svc" style="left:794px"><div class="pic" role="img" aria-label="Blue toned highway with trucks and digital logistics graphics" style="background:linear-gradient(160deg,#cfe2f2,#5f8fbf 55%,#2a4a72)"></div><h4>Unparalleled customer focus</h4><p>We live a customer-oriented mindset, always measuring ourselves against their experience</p></div>
</section>

<!-- CTA -->
<section class="abs cta">
  <h2>Get in touch with Brook Logistics</h2>
  <p>If you got excited, or have a question about our services, our approach, our jobs or just want to get in touch to chat about how green logistics can make the planet a little bit better, please get in touch!</p>
  <a class="btn">Contact Us</a>
</section>

<!-- Careers -->
<h2 class="abs sec-title" style="top:2259px">Careers</h2>
<svg class="abs rule" style="top:2292px" viewBox="0 0 84 10"><line x1="0" y1="5" x2="30" y2="5" stroke="#3aa935"/><line x1="54" y1="5" x2="84" y2="5" stroke="#3aa935"/><path d="M36 8c2-6 8-7 12-6-1 5-6 7-12 6z" fill="#3aa935"/></svg>

<div class="abs careers-left">
  <p>If you join Brook Logistics, you join a family. We elevate one another, care for each other's wellbeing and growth, and celebrate our successes. We strongly believe growth is a team sport and that every member of the family fully contributes to the achievements of the company overall</p>
  <p>At the heart of everything we do at Brook Logistics is a relentless focus on our mission. That's why we aim to ensure our employees can follow their own passion at the workplace, be this working in a truly collaborative and caring team, putting a smile on a customer's face or making the world a better place.</p>
  <p>While we are helping our clients grow by delivering their parcels, we are also helping all our employees grow personally and professionally. We care about our employees' happiness and wellbeing which is why we provide additional benefits like supplementary health insurance.</p>
  <div class="short"></div>
  <em>We offer a secure and varied job in a rapidly growing company with opportunities for advancement.</em>
  <div class="interest">INTERESTED?</div>
  <div>We would like to invite you to a trial day.</div>
</div>
<a class="abs btn" style="left:225px;top:2703px;width:156px;height:32px;font-size:11px">Send Us an Email</a>
<a class="abs btn-out" style="left:394px;top:2703px;width:156px;height:32px">Give Us a Call</a>

<div class="abs careers-right">If you are excited about joining our Brook Logistics family,<br>please check out our open positions.</div>
<div class="abs acc" style="top:2390px;height:28px"><span>Full-time driver / parcel deliverer (m/f/d) for Berlin</span><span>+</span></div>
<div class="abs acc open" style="top:2433px;height:28px;border-bottom:none"><span>Your tasks as a delivery driver:</span><span style="color:#999">-</span></div>
<ul class="abs panel">
  <li><svg width="9" height="7" viewBox="0 0 9 7"><path d="M1 3.5 3.5 6 8 1" fill="none" stroke="#3aa935" stroke-width="1.6"/></svg>Delivery of packages to end customers</li>
  <li><svg width="9" height="7" viewBox="0 0 9 7"><path d="M1 3.5 3.5 6 8 1" fill="none" stroke="#3aa935" stroke-width="1.6"/></svg>In the delivery center: preparation of the tour and loading of the delivery van with parcels</li>
  <li><svg width="9" height="7" viewBox="0 0 9 7"><path d="M1 3.5 3.5 6 8 1" fill="none" stroke="#3aa935" stroke-width="1.6"/></svg>Drive from the delivery center to the delivery area - you will be guided by a navigation system</li>
  <li><svg width="9" height="7" viewBox="0 0 9 7"><path d="M1 3.5 3.5 6 8 1" fill="none" stroke="#3aa935" stroke-width="1.6"/></svg>Delivery of the parcels to end customers in the delivery area - the navigation helps you here too</li>
  <li><svg width="9" height="7" viewBox="0 0 9 7"><path d="M1 3.5 3.5 6 8 1" fill="none" stroke="#3aa935" stroke-width="1.6"/></svg>Suggest ideas for improvement in the delivery process</li>
  <li><svg width="9" height="7" viewBox="0 0 9 7"><path d="M1 3.5 3.5 6 8 1" fill="none" stroke="#3aa935" stroke-width="1.6"/></svg>Take care of and charge the delivery van</li>
</ul>
<div class="abs acc" style="top:2680px;height:28px"><span>Required knowledge and skills:</span><span>+</span></div>
<div class="abs acc" style="top:2721px;height:29px"><span>What you can expected from the Brook Logistics family:</span><span>+</span></div>

<!-- Contact -->
<section class="abs contact" role="img" aria-label="Dark background fading into a field of green grass">
  <h2>Contact Us</h2>
  <svg class="abs rule" style="top:85px" viewBox="0 0 84 10"><line x1="0" y1="5" x2="30" y2="5" stroke="#3aa935"/><line x1="54" y1="5" x2="84" y2="5" stroke="#3aa935"/><path d="M36 8c2-6 8-7 12-6-1 5-6 7-12 6z" fill="#3aa935"/></svg>
  <p class="lead">We'd love to hear from you!</p>
  <p class="note">Whether you have a question about our services, our approach, our jobs or just want to get in touch to chat about how green logistics can make the planet a little bit better, our team is ready to answer your questions and enquiries.</p>

  <div class="abs info" style="top:221px"><span class="ic"><svg width="14" height="16" viewBox="0 0 14 18"><path d="M7 1a6 6 0 0 1 6 6c0 4-6 10-6 10S1 11 1 7a6 6 0 0 1 6-6z" fill="#3aa935"/><circle cx="7" cy="7" r="2.2" fill="#fff"/></svg></span><span>LOCATION:<br>United States of America</span></div>
  <div class="abs info" style="top:289px"><span class="ic"><svg width="15" height="11" viewBox="0 0 15 11"><rect x=".7" y=".7" width="13.6" height="9.6" rx="1" fill="none" stroke="#3aa935" stroke-width="1.4"/><path d="M1 1l6.5 5L14 1" fill="none" stroke="#3aa935" stroke-width="1.4"/></svg></span><span>EMAIL ADDRESS:<br>hello@brooklogistics.com</span></div>
  <div class="abs info" style="top:358px"><span class="ic"><svg width="14" height="14" viewBox="0 0 24 24"><path d="M6.6 10.8a15 15 0 0 0 6.6 6.6l2.2-2.2c.3-.3.7-.4 1-.2 1.1.4 2.3.6 3.6.6.6 0 1 .4 1 1V20c0 .6-.4 1-1 1A17 17 0 0 1 3 4c0-.6.4-1 1-1h3.5c.6 0 1 .4 1 1 0 1.3.2 2.5.6 3.6.1.3 0 .7-.2 1z" fill="#3aa935"/></svg></span><span>CALL US:<br>(555) 014-2290</span></div>

  <div class="abs field" style="left:544px;top:209px;width:209px;height:30px">Your Name</div>
  <div class="abs field" style="left:766px;top:209px;width:209px;height:30px">Subject</div>
  <div class="abs field" style="left:544px;top:253px;width:431px;height:123px">Message</div>
  <a class="btn">Send Message</a>

  <div class="abs footer-line"></div>
  <div class="abs foot" style="left:225px"><u>Legal Notice</u><u>Privacy Policy</u></div>
  <div class="abs foot" style="left:495px">Copyright © Brook Logistics 2020. All rights reserved.</div>
  <span class="abs social" style="left:856px" aria-label="Social profile link"></span>
  <span class="abs social" style="left:899px" aria-label="Social profile link"></span>
  <span class="abs social" style="left:943px" aria-label="Social profile link"></span>
</section>

</body>
</html>
```